Business Card for my Photography/Video Business

I would like the card to say Event Photographer and Videographer. I like the Black and Gold look to it as well but open to other options. I don't want it to be super vibrant or colorful. Simple, elegant and professional

```html
<!DOCTYPE html>
<html lang="en">
<head>
<meta charset="UTF-8">
<title>Orin Films – Business Card</title>
<link href="https://fonts.googleapis.com/css2?family=Jost:wght@400;500;600&display=swap" rel="stylesheet">
<style>
  :root {
    --backdrop: #2b2b2b;
    --card-light: #e4e4e4;
    --card-dark: #161616;
    --ink: #1f1f1f;
    --ink-soft: #2e2e2e;
    --gold: #c8a24c;
    --gold-muted: #a8894a;
  }
  * { box-sizing: border-box; margin: 0; padding: 0; }
  html, body {
    width: 1200px;
    height: 600px;
    overflow: hidden;
    background: var(--backdrop);
    font-family: "Jost", sans-serif;
  }
  .canvas {
    position: relative;
    width: 1200px;
    height: 600px;
  }
  .card {
    position: absolute;
    top: 90px;
    width: 420px;
    height: 420px;
    border-radius: 22px;
  }
  .card--front { left: 155px; background: var(--card-light); color: var(--ink); }
  .card--back  { left: 625px; background: var(--card-dark); color: var(--gold); }

  .brand {
    position: absolute;
    left: 0; right: 0;
    display: flex;
    align-items: center;
    justify-content: center;
    font-weight: 500;
    letter-spacing: 0.04em;
  }
  .brand__dot { border-radius: 50%; flex: none; }
  .card--front .brand { top: 80px; font-size: 29px; gap: 10px; color: var(--ink-soft); }
  .card--front .brand__dot { width: 48px; height: 48px; background: var(--ink-soft); }
  .card--back .brand { top: 158px; font-size: 44px; gap: 14px; color: var(--gold); }
  .card--back .brand__dot { width: 82px; height: 82px; background: var(--gold); }

  .person {
    position: absolute;
    top: 213px;
    left: 0; right: 0;
    text-align: center;
    line-height: 1;
  }
  .person__first { font-size: 25px; font-weight: 400; letter-spacing: 0.01em; }
  .person__last  { font-size: 25px; font-weight: 600; letter-spacing: 0.01em; margin-top: 1px; }
  .person__title { font-size: 15px; font-weight: 500; margin-top: 14px; letter-spacing: 0.02em; }

  .contact {
    position: absolute;
    top: 340px;
    left: 0; right: 0;
    display: flex;
    justify-content: center;
    gap: 18px;
    font-size: 16px;
  }
  .contact__item { display: flex; align-items: center; gap: 10px; }
  .contact__icon { width: 18px; height: 14px; fill: var(--ink); }

  .website {
    position: absolute;
    top: 286px;
    left: 0; right: 0;
    text-align: center;
    font-size: 12.5px;
    letter-spacing: 0.22em;
    color: var(--gold-muted);
  }
</style>
</head>
<body>
<main class="canvas">
  <section class="card card--front">
    <div class="brand"><span class="brand__dot"></span><span class="brand__name">ORIN FILMS</span></div>
    <div class="person">
      <p class="person__first">FIRSTNAME</p>
      <p class="person__last">LASTNAME</p>
      <p class="person__title">JOB TITLE</p>
    </div>
    <div class="contact">
      <span class="contact__item">
        <svg class="contact__icon" viewBox="0 0 18 14" aria-hidden="true">
          <path d="M1 5 C1 1.5 17 1.5 17 5 L17 6.5 L13 6.5 L13 4.6 C11 3.8 7 3.8 5 4.6 L5 6.5 L1 6.5 Z"/>
          <path d="M4 8 L6.5 5.5 L11.5 5.5 L14 8 L14 13 L4 13 Z"/>
        </svg>
        000 000 0000
      </span>
      <span class="contact__item">
        <svg class="contact__icon" viewBox="0 0 18 14" aria-hidden="true">
          <path d="M1 1 H17 V13 H1 Z M2.5 2.5 L9 7.5 L15.5 2.5 Z"/>
        </svg>
        youremail@xyz.com
      </span>
    </div>
  </section>

  <section class="card card--back">
    <div class="brand"><span class="brand__dot"></span><span class="brand__name">ORIN FILMS</span></div>
    <p class="website">www.yourwebsite.com</p>
  </section>
</main>
</body>
</html>
```